nine-parts.com

We are a small dollar lending company that will revolutionize the industry. We will do this by being completely transparent, fee free, etc and an interest rate that normal people can afford to pay. Over 10X less than our competition. We only allow our members to pay bills " bills paid fast", within 72 hours. Payday loans typically charge from 390%-600% with a terrible payback structure. We charge 36%, period, with a payback structure over 12 months. Our site will be very simple and easy to use but elegant at the same time. We do not want the site to be too busy, less is more and easier. We will have; Home, The Story, Why 9parts.com, Are you eligible? Members, Clients. To become a member you have to be referred by a current client of 9parts.com. A lot of the busy stuff will be saved for the Members and Clients sections. The feel must be elegant, easy to use and very simple to understand. I am looking for the green, white and black combinations of colors, very similar to my logo that was designed by Pixelmoor.

```html
<!DOCTYPE html>
<html lang="en">
<head>
<meta charset="utf-8">
<title>nine-parts.com</title>
<link rel="stylesheet" href="https://fonts.googleapis.com/css2?family=Open+Sans:wght@300;400;600;700&display=swap">
<style>
:root{
  --green:#4cbb3a;
  --green-dark:#35a12a;
  --green-light:#8fdc5e;
  --ink:#2b2b2b;
  --text:#666;
  --muted:#999;
  --line:#e3e3e3;
  --band:#f4f5f4;
  --white:#fff;
  --map-base:#ebe7df;
  --map-park:#cfe3b8;
  --map-water:#c4d9e6;
}
*{box-sizing:border-box;margin:0;padding:0}
html,body{width:1200px;height:2248px;overflow:hidden}
body{position:relative;background:var(--white);font-family:"Open Sans",Arial,sans-serif;color:var(--text)}
.abs{position:absolute}

/* header */
.site-header{left:0;top:0;width:1200px;height:84px;background:var(--white);border-bottom:1px solid var(--line)}
.brand{left:120px;top:20px;display:flex;align-items:center;gap:10px;font-size:22px;font-weight:700;color:var(--green)}
.brand-dot{width:34px;height:34px;border-radius:50%;border:3px solid var(--green)}
.top-contact{right:120px;top:8px;font-size:11px;color:var(--muted);display:flex;gap:26px}
.main-nav{right:120px;top:52px;display:flex;font-size:12px}
.main-nav a{display:block;padding:9px 16px;color:var(--text);text-decoration:none}
.main-nav a.active{background:var(--green);color:var(--white)}

/* hero */
.hero{left:0;top:84px;width:1200px;height:488px;background:radial-gradient(ellipse at 60% 35%,#a8ea74 0%,var(--green-light) 30%,var(--green) 75%,var(--green-dark) 100%);overflow:hidden}
.hero-photo{left:110px;top:20px;width:460px;height:468px;background:radial-gradient(ellipse 45% 55% at 50% 60%,rgba(30,90,35,.38) 0%,rgba(40,110,40,.22) 45%,rgba(76,187,58,0) 75%)}
.hero-copy{left:730px;top:120px;width:340px;text-align:center;color:var(--white)}
.hero-copy h1{font-size:64px;font-weight:300;line-height:1}
.hero-copy p{font-size:14px;line-height:1.5;margin-top:14px}
.hero-btn{display:inline-block;margin-top:18px;padding:6px 16px;background:var(--white);color:var(--green);font-size:11px;font-weight:600;border-radius:2px}
.hero-arrow{top:226px;width:22px;height:34px;background:rgba(255,255,255,.85)}
.hero-dots{left:620px;top:440px;display:flex;gap:8px}
.hero-dots span{width:8px;height:8px;border-radius:50%;background:rgba(255,255,255,.5)}
.hero-dots span.on{background:var(--white)}

/* features */
.features{left:100px;top:610px;width:1000px;display:flex;gap:40px}
.feature{width:220px}
.feature-head{display:flex;align-items:center;gap:12px}
.feature-icon{width:40px;height:40px;background:var(--green);display:flex;align-items:center;justify-content:center}
.feature h3{font-size:20px;font-weight:400;color:var(--ink)}
.feature p{font-size:11px;line-height:1.6;margin-top:14px;color:var(--muted)}
.feature .more{font-size:11px;color:var(--ink);margin-top:12px;display:block}

/* stats */
.stats{left:0;top:800px;width:1200px;height:124px;background:var(--band);border-top:1px solid var(--line);border-bottom:1px solid var(--line)}
.stat{top:22px;width:220px}
.stat b{display:block;font-size:52px;font-weight:300;color:var(--green);line-height:1}
.stat span{font-size:11px;color:var(--muted)}

/* sections */
.ring{width:56px;height:56px;border-radius:50%;border:2px solid var(--green);display:flex;align-items:center;justify-content:center;left:572px}
.section-title{left:0;width:1200px;text-align:center;font-size:26px;font-weight:300;color:var(--ink);letter-spacing:1px}
.rule{left:560px;width:80px;height:1px;background:var(--line)}
.section-text{left:170px;width:860px;text-align:center;font-size:11px;line-height:1.7;color:var(--muted)}

/* testimonials & bill pay */
.col-title{font-size:16px;font-weight:400;color:var(--ink);letter-spacing:1px;padding-bottom:10px;border-bottom:1px solid var(--line);width:400px}
.testimonial{left:120px;top:1300px;width:400px;font-size:11px;line-height:1.6}
.testimonial .lead{color:var(--green)}
.avatar{left:130px;top:1380px;width:110px;height:110px;border-radius:50%;background:linear-gradient(160deg,#d9c9bd,#8d7769)}
.quote{left:270px;top:1395px;width:250px;font-size:11px;line-height:1.6}
.read-btn{left:270px;top:1496px;padding:5px 12px;background:var(--green);color:var(--white);font-size:10px}
.t-dots{left:160px;top:1546px;display:flex;gap:6px}
.t-dots span{width:6px;height:6px;border-radius:50%;background:#ccc}
.t-dots span.on{background:var(--green)}
.pay-line{left:741px;top:1320px;width:1px;height:210px;background:var(--line)}
.pay-step{left:720px;width:400px;display:flex;gap:18px}
.pay-icon{width:44px;height:44px;border-radius:50%;border:1px solid #ccc;background:var(--white);flex:none;display:flex;align-items:center;justify-content:center}
.pay-step h4{font-size:12px;font-weight:400;color:var(--green)}
.pay-step p{font-size:10px;line-height:1.6;color:var(--muted);margin-top:2px}

/* clients */
.clients{left:100px;top:1852px;width:1000px;height:56px;display:flex;align-items:center;justify-content:space-between}
.c-arrow{width:22px;height:22px;background:var(--green)}
.client{font-size:20px;font-weight:600;color:#555;display:flex;align-items:center;gap:8px}
.client i{width:22px;height:22px;background:#777;display:block}

/* map + footer */
.map{left:0;top:1920px;width:1200px;height:280px;background:
  radial-gradient(ellipse 18% 30% at 15% 70%,var(--map-park),rgba(207,227,184,0) 100%),
  radial-gradient(ellipse 14% 22% at 78% 25%,var(--map-park),rgba(207,227,184,0) 100%),
  radial-gradient(ellipse 22% 40% at 55% 85%,var(--map-water),rgba(196,217,230,0) 100%),
  linear-gradient(135deg,#efece5,var(--map-base) 55%,#e4e0d6)}
.map-label{left:14px;top:12px;padding:5px 9px;background:var(--white);border:1px solid #ccc;font-size:10px;color:#444}
.site-footer{left:0;top:2200px;width:1200px;height:48px;background:var(--band);border-top:1px solid var(--line)}
.footer-copy{left:120px;top:16px;font-size:11px;color:var(--muted)}
.footer-copy b{color:var(--green)}
.social{right:120px;top:10px;display:flex;gap:8px}
.social span{width:26px;height:26px;border-radius:50%;background:var(--green)}
</style>
</head>
<body>

<header class="site-header abs">
  <div class="brand abs"><span class="brand-dot"></span>9parts</div>
  <div class="top-contact abs"><span>☎ 0800 555 0194</span><span>✉ hello@nine-parts.com</span></div>
  <nav class="main-nav abs">
    <a class="active">Home</a><a>The Story</a><a>Why 9parts.com</a><a>Are you eligible</a><a>Members</a><a>Clients</a>
  </nav>
</header>

<section class="hero abs">
  <div class="hero-photo abs" role="img" aria-label="Photo of two smiling young members holding phones"></div>
  <div class="hero-arrow abs" style="left:0"><svg width="22" height="34"><path d="M13 11l-6 6 6 6" fill="none" stroke="#4cbb3a" stroke-width="2"/></svg></div>
  <div class="hero-arrow abs" style="right:0"><svg width="22" height="34"><path d="M9 11l6 6-6 6" fill="none" stroke="#4cbb3a" stroke-width="2"/></svg></div>
  <div class="hero-copy abs">
    <h1>36%</h1>
    <p>To become a member you have to be referred by<br>a current client of 9parts.com</p>
    <span class="hero-btn">Sign Now</span>
  </div>
  <div class="hero-dots abs"><span class="on"></span><span></span><span></span></div>
</section>

<section class="features abs">
  <div class="feature">
    <div class="feature-head"><span class="feature-icon"><svg width="20" height="20"><circle cx="10" cy="10" r="8" fill="none" stroke="#fff" stroke-width="2"/></svg></span><h3>Lovely</h3></div>
    <p>Simple terms explained clearly so every member knows exactly what they pay.</p><span class="more">Details ›</span>
  </div>
  <div class="feature">
    <div class="feature-head"><span class="feature-icon"><svg width="20" height="20"><path d="M3 10l5 5 9-10" fill="none" stroke="#fff" stroke-width="2"/></svg></span><h3>Exquisite</h3></div>
    <p>No hidden fees and no surprises, just one fair rate for the full year.</p><span class="more">Details ›</span>
  </div>
  <div class="feature">
    <div class="feature-head"><span class="feature-icon"><svg width="20" height="20"><rect x="3" y="8" width="3" height="9" fill="#fff"/><rect x="9" y="5" width="3" height="12" fill="#fff"/><rect x="15" y="2" width="3" height="15" fill="#fff"/></svg></span><h3>Glorious</h3></div>
    <p>Bills paid fast, within seventy two hours of your approved request.</p><span class="more">Details ›</span>
  </div>
  <div class="feature">
    <div class="feature-head"><span class="feature-icon"><svg width="20" height="20"><path d="M10 2l8 15H2z" fill="#fff"/></svg></span><h3>Stunning</h3></div>
    <p>Payback spread across twelve months so repayments stay easy to manage.</p><span class="more">Details ›</span>
  </div>
</section>

<section class="stats abs">
  <div class="stat abs" style="left:100px"><b>365</b><span>Days worked</span></div>
  <div class="stat abs" style="left:360px"><b>2500+</b><span>satisfied clients</span></div>
  <div class="stat abs" style="left:620px"><b>3679+</b><span>bills already paid</span></div>
  <div class="stat abs" style="left:880px"><b>150+</b><span>Team Members</span></div>
</section>

<div class="ring abs" style="top:990px"><svg width="24" height="24"><path d="M4 12l6 6 10-12" fill="none" stroke="#4cbb3a" stroke-width="2"/></svg></div>
<h2 class="section-title abs" style="top:1058px">WELCOME</h2>
<div class="rule abs" style="top:1100px"></div>
<p class="section-text abs" style="top:1112px">We are a small dollar lending company built on being completely transparent and fee free, with an interest rate that normal people can afford to pay. Our members pay bills fast, within 72 hours, at a flat 36% with a simple payback structure over twelve months. No busy fine print, no surprises, just an honest way to cover the bills that matter most and keep life moving forward with confidence.</p>

<div class="abs" style="left:120px;top:1255px"><h3 class="col-title">TESTIMONIALS</h3></div>
<div class="testimonial abs"><p class="lead">Lorem member since spring</p><p>Quick approval and a fair rate made this month far easier to handle.</p></div>
<div class="avatar abs" role="img" aria-label="Portrait photo of a satisfied member"></div>
<p class="quote abs">They paid my electric bill within two days. The monthly payments are small and clear, and I never felt pressured at any point. I recommend them to friends.</p>
<span class="read-btn abs">Read More</span>
<div class="t-dots abs"><span class="on"></span><span></span><span></span></div>

<div class="abs" style="left:700px;top:1255px"><h3 class="col-title">POST BILL PAY</h3></div>
<div class="pay-line abs"></div>
<div class="pay-step abs" style="top:1300px"><span class="pay-icon"><svg width="18" height="18"><path d="M9 2a5 5 0 015 5c0 4-5 9-5 9s-5-5-5-9a5 5 0 015-5z" fill="none" stroke="#999" stroke-width="1.5"/></svg></span><div><h4>In Person at any post office</h4><p>Bring your member card and bill to the counter<br>and we settle it the same week.</p></div></div>
<div class="pay-step abs" style="top:1400px"><span class="pay-icon"><svg width="18" height="18"><circle cx="9" cy="9" r="7" fill="none" stroke="#999" stroke-width="1.5"/><path d="M9 5v4l3 2" fill="none" stroke="#999" stroke-width="1.5"/></svg></span><div><h4>By Phone payment</h4><p>Call our member line and a team member<br>will pay the bill for you directly.</p></div></div>
<div class="pay-step abs" style="top:1500px"><span class="pay-icon"><svg width="18" height="18"><rect x="2" y="3" width="14" height="10" fill="none" stroke="#999" stroke-width="1.5"/><path d="M6 16h6" stroke="#999" stroke-width="1.5"/></svg></span><div><h4>On the Internet</h4><p>Log in to the members area and submit<br>the bill online in a few clicks.</p></div></div>

<div class="ring abs" style="top:1688px"><svg width="24" height="24"><circle cx="9" cy="9" r="4" fill="none" stroke="#4cbb3a" stroke-width="2"/><path d="M2 21c1-5 13-5 14 0" fill="none" stroke="#4cbb3a" stroke-width="2"/></svg></div>
<h2 class="section-title abs" style="top:1752px">OUR CLIENTS</h2>
<p class="section-text abs" style="top:1796px">Trusted by local businesses and families who value fair and simple lending.</p>

<div class="clients abs">
  <span class="c-arrow"><svg width="22" height="22"><path d="M13 6l-5 5 5 5" fill="none" stroke="#fff" stroke-width="2"/></svg></span>
  <span class="client">Fernwick</span>
  <span class="client"><i></i>Lumora</span>
  <span class="client">Brightleaf</span>
  <span class="client"><i></i>Northgate Studio</span>
  <span class="client">The Ledger</span>
  <span class="c-arrow"><svg width="22" height="22"><path d="M9 6l5 5-5 5" fill="none" stroke="#fff" stroke-width="2"/></svg></span>
</div>

<div class="map abs" role="img" aria-label="Street map of the city around the office location">
  <span class="map-label abs">View larger map</span>
</div>

<footer class="site-footer abs">
  <p class="footer-copy abs"><b>nine-parts.com</b> © 2014 All rights reserved · Privacy Policy</p>
  <div class="social abs"><span></span><span></span><span></span><span></span></div>
</footer>

</body>
</html>
```